Bref créative
Safety products company
Safety products for life
Professional
Gordon R Pike
President/Founder
482 Wexley Lane
Marlow Hollow, PA 16224-3871
866.41C.TOWN (412.8696)
pike@corvantahome.com
www.corvantahome.com
BE PREPARED
HOME
DISASTER
CHILD
SENIOR
PET
TRAVEL
LIVE SAFELY
the logo
"stacked" logo - two more will be coming with white backgrounds as soon as I receive them
4 AI LOGOS

```html
<!DOCTYPE html>
<html lang="en">
<head>
<meta charset="utf-8">
<title>Corvanta Home – Stationery</title>
<link rel="stylesheet" href="https://fonts.googleapis.com/css2?family=Arimo:wght@400;700&display=swap">
<style>
  :root {
    --page: #ffffff;
    --frame: #d9d9d9;
    --paper: #ffffff;
    --paper-edge: #cfcfcf;
    --band: #121212;
    --accent: #d8262c;
    --accent-soft: #e86a3a;
    --ink-light: #e8e8e8;
    --ink-muted: #9a9a9a;
  }
  * { box-sizing: border-box; margin: 0; padding: 0; }
  html, body { width: 1200px; height: 681px; overflow: hidden; background: var(--page); }
  body { font-family: "Arimo", Arial, sans-serif; position: relative; }

  .sheet-frame {
    position: absolute; left: 12px; top: 12px; width: 1176px; height: 657px;
    border: 1px solid var(--frame);
  }
  .piece { position: absolute; background: var(--paper); border: 1px solid var(--paper-edge); overflow: hidden; }

  .band { position: absolute; left: 0; right: 0; background: var(--band); }
  .band::before, .band::after {
    content: ""; position: absolute; left: 0; right: 0; height: 2px;
    background: linear-gradient(90deg, var(--accent), var(--accent-soft) 40%, #666 100%);
  }
  .band::before { top: 4px; }
  .band::after { bottom: 4px; }

  .brand {
    position: absolute; display: flex; align-items: center; gap: 7px;
    color: var(--ink-light); font-weight: 700; letter-spacing: 0.08em; white-space: nowrap;
  }
  .brand-dot { width: 14px; height: 14px; border-radius: 50%; background: var(--accent); flex: none; }

  .contact {
    position: absolute; color: var(--ink-light); font-size: 6.5px; line-height: 8.4px; white-space: nowrap;
  }

  /* envelope front */
  .envelope-front { left: 65px; top: 101px; width: 492px; height: 211px; }
  .envelope-front .band { top: 12px; height: 84px; }
  .envelope-front .brand { left: 22px; top: 48px; font-size: 15px; }
  .envelope-front .contact { left: 362px; top: 20px; }

  /* envelope back */
  .envelope-back { left: 65px; top: 360px; width: 492px; height: 211px; }
  .envelope-back .flap { position: absolute; left: 0; top: 0; width: 492px; height: 90px; }
  .envelope-back .brand { left: 50%; top: 30px; transform: translateX(-50%); font-size: 13px; }

  /* letterhead */
  .letterhead { left: 619px; top: 113px; width: 312px; height: 516px; }
  .letterhead .band { top: 20px; height: 52px; }
  .letterhead .brand { left: 10px; top: 14px; font-size: 11px; gap: 5px; }
  .letterhead .brand-dot { width: 11px; height: 11px; }
  .letterhead .contact { left: 188px; top: 9px; font-size: 5.2px; line-height: 6.6px; }

  /* business cards */
  .card { background: var(--band); border-color: var(--band); }
  .card-front { left: 955px; top: 235px; width: 166px; height: 89px; }
  .card-front .brand { left: 8px; top: 40px; font-size: 6px; gap: 3px; letter-spacing: 0.04em; }
  .card-front .brand-dot { width: 8px; height: 8px; }
  .card-front .person { position: absolute; left: 96px; top: 12px; color: var(--ink-light); }
  .person-name { font-size: 6px; font-weight: 700; line-height: 8px; }
  .person-title { font-size: 4.6px; color: var(--ink-muted); line-height: 7px; margin-bottom: 3px; }
  .card-front .contact { position: static; font-size: 4.3px; line-height: 6px; }

  .card-back { left: 955px; top: 360px; width: 166px; height: 91px; }
  .card-back .brand { left: 50%; top: 24px; transform: translateX(-50%); font-size: 8px; gap: 4px; }
  .card-back .brand-dot { width: 9px; height: 9px; }
  .card-back .categories {
    position: absolute; left: 0; right: 0; top: 58px; text-align: center;
    color: var(--ink-light); font-size: 4.6px; letter-spacing: 0.04em;
  }
</style>
</head>
<body>
  <div class="sheet-frame"></div>

  <section class="piece envelope-front" aria-label="Envelope front">
    <div class="band">
      <div class="brand"><span class="brand-dot"></span>CORVANTA HOME</div>
      <div class="contact">
        482 Wexley Lane<br>
        Marlow Hollow, PA 16224-3871<br>
        866.41C.TOWN (412.8696)<br>
        pike@corvantahome.com<br>
        www.corvantahome.com
      </div>
    </div>
  </section>

  <section class="piece envelope-back" aria-label="Envelope back">
    <svg class="flap" viewBox="0 0 492 90" aria-hidden="true">
      <path d="M0 0 H492 V40 Q440 44 300 84 Q246 96 192 84 Q52 44 0 40 Z" fill="#121212"/>
    </svg>
    <div class="brand"><span class="brand-dot"></span>CORVANTA HOME</div>
  </section>

  <section class="piece letterhead" aria-label="Letterhead">
    <div class="band">
      <div class="brand"><span class="brand-dot"></span>CORVANTA HOME</div>
      <div class="contact">
        482 Wexley Lane<br>
        Marlow Hollow, PA 16224-3871<br>
        866.41C.TOWN (412.8696)<br>
        pike@corvantahome.com<br>
        www.corvantahome.com
      </div>
    </div>
  </section>

  <section class="piece card card-front" aria-label="Business card front">
    <div class="brand"><span class="brand-dot"></span>CORVANTA HOME</div>
    <div class="person">
      <div class="person-name">Gordon R Pike</div>
      <div class="person-title">President/Founder</div>
      <div class="contact">
        482 Wexley Lane<br>
        Marlow Hollow, PA 16224-3871<br>
        866.41C.TOWN (412.8696)<br>
        pike@corvantahome.com<br>
        www.corvantahome.com
      </div>
    </div>
  </section>

  <section class="piece card card-back" aria-label="Business card back">
    <div class="brand"><span class="brand-dot"></span>CORVANTA HOME</div>
    <div class="categories">Home · Disaster · Child · Senior · Pet · Travel</div>
  </section>
</body>
</html>
```